Complete redesign of Licensed Medical Cannabis Dispensary website

Redesign website to modernize it and simplify it and add a self service reservation/preorder interactive delivery form. Also integrate current POS system that has current inventory. Here is a website for inspiration that I really like because of it simplicity https://www.lumo.example and easy ordering option. Attached is our logo.... please design around that and this is our website address www.brindlegatecourier.example

Font styles to use
Sans Serif

Colors
5c5c5c
cbcbcb
000000
add136

Requirements
Must have
• inventory thats integrated with pos
• online reservation/delivery form
Nice to have
• a website thats modern and simple
• The website designed are the logo that is attached
Should not have
• too much information

```html
<!DOCTYPE html>
<html lang="en">
<head>
<meta charset="utf-8">
<title>Brindlegate – Medical Delivery</title>
<link href="https://fonts.googleapis.com/css2?family=Open+Sans:ital,wght@0,400;0,600;0,700;1,400&display=swap" rel="stylesheet">
<style>
:root{
  --green:#add136;
  --grey:#5c5c5c;
  --light:#cbcbcb;
  --black:#000000;
  --ink:#333333;
  --muted:#888888;
  --line:#e8e8e8;
  --page:#f4f4f4;
  --white:#ffffff;
}
*{box-sizing:border-box;margin:0;padding:0}
html,body{width:725px;height:1200px;overflow:hidden}
body{font-family:"Open Sans",sans-serif;color:var(--ink);background:var(--white);position:relative;font-size:7px}

/* header */
.site-header{position:absolute;top:0;left:0;width:725px;height:58px;border-bottom:1px solid var(--line)}
.brand{position:absolute;left:99px;top:18px;display:flex;align-items:center;gap:6px}
.brand-mark{width:22px;height:22px;border-radius:50%;background:var(--green)}
.brand-name{font-size:15px;font-weight:600;color:var(--green);line-height:1}
.search{position:absolute;left:287px;top:17px;width:207px;height:25px;border:1px solid var(--green);border-radius:13px;display:flex;align-items:center}
.search-input{flex:1;padding-left:9px;font-size:5px;color:var(--muted)}
.search-cat{width:70px;height:100%;border-left:1px solid var(--line);font-size:5px;color:var(--muted);display:flex;align-items:center;padding-left:7px}
.search-btn{width:25px;height:25px;border-radius:50%;background:var(--green);margin-right:-1px;display:flex;align-items:center;justify-content:center}
.header-tools{position:absolute;left:552px;top:19px;display:flex;align-items:center;gap:14px}
.account{font-size:6px;font-weight:600;line-height:1.2;color:var(--ink)}
.account span{display:block;font-weight:400;color:var(--muted)}

/* nav */
.main-nav{position:absolute;top:58px;left:0;width:725px;height:23px;border-bottom:1px solid var(--line)}
.main-nav ul{list-style:none;position:absolute;left:108px;top:0;display:flex;height:23px;align-items:center;gap:20px}
.main-nav li{font-size:5.6px;color:var(--ink)}
.main-nav li.active{color:var(--green)}
.orders{position:absolute;right:98px;top:8px;font-size:5.6px;display:flex;align-items:center;gap:4px}
.orders b{font-weight:700}

/* hero */
.hero{position:absolute;top:82px;left:0;width:725px;height:161px;background:#f1f1f1;overflow:hidden}
.hero-photo{position:absolute;left:330px;top:0;width:395px;height:161px;background:radial-gradient(ellipse at 45% 55%,#6b7d3a 0%,#8f9d5a 35%,#cfcfbf 70%,#efefef 100%)}
.hero-photo::after{content:"";position:absolute;right:0;top:0;width:90px;height:80px;background:radial-gradient(circle at 70% 30%,#e9a545,#f0c77a 50%,transparent 75%)}
.hero-copy{position:absolute;left:97px;top:26px}
.hero-title{font-size:16.5px;font-weight:700;line-height:1.2;color:var(--black);letter-spacing:.2px}
.hero-text{font-size:10.5px;line-height:1.4;margin-top:3px;color:var(--black)}
.hero-actions{display:flex;gap:8px;margin-top:12px}
.btn{height:22px;border-radius:11px;font-size:5.6px;font-weight:700;color:var(--white);display:flex;align-items:center;justify-content:center;width:77px;text-transform:uppercase}
.btn-shop{background:var(--green)}
.btn-verify{background:var(--grey)}
.hero-arrow{position:absolute;top:72px;width:18px;height:18px;background:#8a8a8a;display:flex;align-items:center;justify-content:center}

/* steps */
.steps{position:absolute;top:243px;left:0;width:725px;height:98px;background:var(--grey)}
.step{position:absolute;top:14px;width:120px;text-align:center;color:var(--white)}
.step-icon{width:28px;height:28px;border-radius:50%;background:var(--white);margin:0 auto;position:relative}
.step-num{position:absolute;left:-6px;top:-3px;width:12px;height:12px;border-radius:50%;background:var(--green);font-size:6px;font-weight:700;line-height:12px;color:var(--white)}
.step h3{font-size:8px;font-weight:700;margin-top:4px}
.step p{font-size:5.6px;line-height:1.55;margin-top:3px}
.step-arrow{position:absolute;top:40px}

/* products */
.catalog{position:absolute;top:341px;left:0;width:725px;height:557px;background:var(--page)}
.grid{position:absolute;left:97px;top:26px;width:530px;display:grid;grid-template-columns:repeat(4,1fr);gap:1px;background:var(--line)}
.product{background:var(--white);height:154px;text-align:center;position:relative}
.product-photo{width:90px;height:86px;margin:14px auto 0;border-radius:40%}
.product-name{font-size:6.4px;font-weight:400;margin-top:11px;color:var(--ink)}
.product-rule{width:14px;height:1px;background:var(--line);margin:5px auto}
.product-price{font-size:6.4px;font-weight:600;color:var(--green)}
.quick-view{position:absolute;left:41px;top:60px;background:var(--white);font-size:5px;padding:3px 6px;box-shadow:0 0 3px rgba(0,0,0,.15)}
.flower{background:radial-gradient(ellipse,#6e7f3a,#8d8d5a 55%,rgba(255,255,255,0) 72%)}
.flower-dark{background:radial-gradient(ellipse,#6f5f5a,#8c8275 55%,rgba(255,255,255,0) 72%)}
.shatter{background:radial-gradient(ellipse,#c99a1a,#dcb23a 50%,rgba(255,255,255,0) 72%)}
.budder{background:radial-gradient(ellipse,#e8a23a,#f0c06a 45%,rgba(255,255,255,0) 70%)}
.cart-photo{border-radius:0;width:116px;height:88px;background:linear-gradient(135deg,#3d3d3d,#6f8a3a 50%,#3d3d3d)}
.load-more{position:absolute;left:310px;top:511px;width:105px;height:20px;border:1px solid var(--grey);font-size:5.6px;font-weight:700;color:var(--grey);display:flex;align-items:center;justify-content:center;background:var(--white)}

/* testimonials */
.testimonials{position:absolute;top:898px;left:0;width:725px;height:102px;border-bottom:1px solid var(--line)}
.eyebrow{position:absolute;left:97px;top:24px;font-size:5px;font-weight:700;letter-spacing:.3px}
.section-title{position:absolute;left:97px;top:30px;font-size:13.5px;font-weight:700;color:var(--black)}
.dots{position:absolute;left:97px;top:72px;display:flex;gap:2px}
.dots i{width:5px;height:5px;border-radius:50%;border:1px solid var(--green)}
.dots i.on{background:var(--green)}
.quote{position:absolute;top:24px;width:180px}
.avatar{position:absolute;left:0;top:0;width:32px;height:32px;background:linear-gradient(135deg,#b9a28a,#7a6a5a)}
.quote-mark{position:absolute;left:24px;top:24px;font-size:14px;font-weight:700;color:var(--green);line-height:1}
.quote h4{margin-left:48px;font-size:8px;font-weight:700;color:var(--black);margin-top:2px}
.quote .role{margin-left:48px;font-size:4.6px;color:var(--green)}
.quote p{margin-left:46px;margin-top:6px;font-size:6.4px;font-style:italic;line-height:1.7;color:var(--grey)}

/* footer */
.site-footer{position:absolute;top:1000px;left:0;width:725px;height:200px}
.col{position:absolute;top:26px;width:130px}
.col h5{font-size:7.5px;font-weight:700;color:var(--black);margin-bottom:9px}
.col li{list-style:none;font-size:6.8px;color:var(--ink);line-height:16.3px}
.label{font-size:6.8px;color:var(--muted);margin-top:-2px}
.phone{font-size:10.5px;font-weight:700;color:var(--green);margin:2px 0 7px}
.email{font-size:6.8px}
.social{display:flex;gap:10px;margin-top:11px}
.social i{width:6px;height:6px;border-radius:50%;display:block}
.news-text{font-size:5.8px;line-height:1.85}
.news-input{width:123px;height:18px;border:1px solid var(--line);margin-top:9px;font-size:4.8px;color:var(--muted);padding-left:5px;display:flex;align-items:center}
.news-btn{width:46px;height:14px;background:var(--green);color:var(--white);font-size:4.6px;font-weight:700;display:flex;align-items:center;justify-content:center;margin-top:8px}
.footer-base{position:absolute;left:97px;top:164px;width:530px;border-top:1px solid var(--line);text-align:center;font-size:5px;padding-top:13px;color:var(--grey)}
</style>
</head>
<body>

<header class="site-header">
  <div class="brand">
    <span class="brand-mark"></span>
    <div class="brand-name">Brindlegate</div>
  </div>
  <div class="search">
    <div class="search-input">I'm looking for...</div>
    <div class="search-cat">All Categories</div>
    <div class="search-btn"><svg width="7" height="7" viewBox="0 0 10 10"><circle cx="4" cy="4" r="3" fill="none" stroke="#fff" stroke-width="1.4"/><line x1="6.3" y1="6.3" x2="9" y2="9" stroke="#fff" stroke-width="1.4"/></svg></div>
  </div>
  <div class="header-tools">
    <svg width="12" height="13" viewBox="0 0 12 13"><path d="M1 4h10v8H1z M4 4V2.5a2 2 0 0 1 4 0V4" fill="none" stroke="#000" stroke-width="1.2"/></svg>
    <div style="display:flex;align-items:center;gap:4px">
      <svg width="13" height="13" viewBox="0 0 13 13"><circle cx="6.5" cy="4" r="3" fill="none" stroke="#000" stroke-width="1.2"/><path d="M1 13c0-3.5 2.5-5 5.5-5s5.5 1.5 5.5 5" fill="none" stroke="#000" stroke-width="1.2"/></svg>
      <div class="account">Log In<span>Register</span></div>
    </div>
  </div>
</header>

<nav class="main-nav">
  <ul>
    <li class="active">HOME</li><li>FLOWERS</li><li>CONCENTRATES</li><li>EDIBLES</li><li>FORUMS</li><li>CONTACT US</li><li>MORE</li>
  </ul>
  <div class="orders">
    <svg width="7" height="7" viewBox="0 0 10 10"><path d="M2 1l2 2-1 1.5a6 6 0 0 0 2.5 2.5L7 6l2 2-1.5 1.5C4 9 1 6 .5 2.5z" fill="none" stroke="#333" stroke-width=".9"/></svg>
    Orders: <b>555-014-2290</b>
  </div>
</nav>

<section class="hero">
  <div class="hero-photo" role="img" aria-label="Cannabis buds spilling from an amber prescription bottle"></div>
  <div class="hero-copy">
    <h1 class="hero-title">TOP SHELF MEDICAL<br>MARIJUANA DELIVERY</h1>
    <p class="hero-text">We offer only the highest quality flowers,<br>edibles and concentrates.</p>
    <div class="hero-actions"><span class="btn btn-shop">Shop now</span><span class="btn btn-verify">Get verified</span></div>
  </div>
  <div class="hero-arrow" style="left:41px"><svg width="6" height="8" viewBox="0 0 6 8"><path d="M5 1L2 4l3 3" fill="none" stroke="#fff"/></svg></div>
  <div class="hero-arrow" style="left:666px"><svg width="6" height="8" viewBox="0 0 6 8"><path d="M1 1l3 3-3 3" fill="none" stroke="#fff"/></svg></div>
</section>

<section class="steps">
  <div class="step" style="left:128px">
    <div class="step-icon"><span class="step-num">1</span><svg width="28" height="28" viewBox="0 0 28 28"><rect x="9" y="8" width="10" height="12" fill="none" stroke="#555"/><line x1="11" y1="11" x2="17" y2="11" stroke="#555"/><line x1="11" y1="14" x2="17" y2="14" stroke="#555"/></svg></div>
    <h3>Get Verified</h3>
    <p>It's fast. It's simple. Just fill out<br>our verification form and get<br>approved in minutes.</p>
  </div>
  <svg class="step-arrow" style="left:245px" width="56" height="14" viewBox="0 0 56 14"><path d="M0 7h53M46 1l7 6-7 6" fill="none" stroke="#fff" stroke-width="1.4"/></svg>
  <div class="step" style="left:296px">
    <div class="step-icon"><span class="step-num">2</span><svg width="28" height="28" viewBox="0 0 28 28"><path d="M9 11h10v9H9z M12 11V9a2 2 0 0 1 4 0v2" fill="none" stroke="#555"/></svg></div>
    <h3>Shop</h3>
    <p>Add the products you want to<br>your shopping cart and check<br>out. No credit card required!</p>
  </div>
  <svg class="step-arrow" style="left:413px" width="56" height="14" viewBox="0 0 56 14"><path d="M0 7h53M46 1l7 6-7 6" fill="none" stroke="#fff" stroke-width="1.4"/></svg>
  <div class="step" style="left:471px">
    <div class="step-icon"><span class="step-num">3</span><svg width="28" height="28" viewBox="0 0 28 28"><rect x="9" y="8" width="7" height="12" fill="none" stroke="#555"/><rect x="17" y="12" width="3" height="6" fill="none" stroke="#555"/></svg></div>
    <h3>Get Medicated</h3>
    <p>Sit back and wait. Our profession-<br>al staff will deliver your medica-<br>tion right to your front door.</p>
  </div>
</section>

<section class="catalog">
  <div class="grid">
    <article class="product"><div class="product-photo flower" role="img" aria-label="Flower bud"></div><span class="quick-view">Quick View</span><h4 class="product-name">Meadow Haze</h4><div class="product-rule"></div><div class="product-price">$35.00</div></article>
    <article class="product"><div class="product-photo flower" role="img" aria-label="Flower bud"></div><h4 class="product-name">Pine Crest</h4><div class="product-rule"></div><div class="product-price">$30.00</div></article>
    <article class="product"><div class="product-photo shatter" role="img" aria-label="Amber shatter concentrate"></div><h4 class="product-name">Harbor Gold Shatter</h4><div class="product-rule"></div><div class="product-price">$35.00</div></article>
    <article class="product"><div class="product-photo budder" role="img" aria-label="Golden budder concentrate"></div><h4 class="product-name">Amberline Budder</h4><div class="product-rule"></div><div class="product-price">$40.00</div></article>

    <article class="product"><div class="product-photo flower" role="img" aria-label="Flower bud"></div><h4 class="product-name">Silver Fern</h4><div class="product-rule"></div><div class="product-price">$15.00 – $30.00</div></article>
    <article class="product"><div class="product-photo flower-dark" role="img" aria-label="Purple-toned flower bud"></div><h4 class="product-name">Dusk Berry (Private Reserve)</h4><div class="product-rule"></div><div class="product-price">$25.00 – $60.00</div></article>
    <article class="product"><div class="product-photo budder" role="img" aria-label="Golden sap concentrate"></div><h4 class="product-name">Sunpeel Shatter</h4><div class="product-rule"></div><div class="product-price">$25.00</div></article>
    <article class="product"><div class="product-photo cart-photo" role="img" aria-label="Vape cartridge with packaging tins"></div><h4 class="product-name" style="margin-top:8px">Citrus Mint Cart</h4><div class="product-rule"></div><div class="product-price">$30.00</div></article>

    <article class="product"><div class="product-photo flower" role="img" aria-label="Flower bud"></div><h4 class="product-name">Meadow Haze</h4><div class="product-rule"></div><div class="product-price">$35.00</div></article>
    <article class="product"><div class="product-photo flower" role="img" aria-label="Flower bud"></div><h4 class="product-name">Pine Crest</h4><div class="product-rule"></div><div class="product-price">$30.00</div></article>
    <article class="product"><div class="product-photo shatter" role="img" aria-label="Amber shatter concentrate"></div><h4 class="product-name">Harbor Gold Shatter</h4><div class="product-rule"></div><div class="product-price">$35.00</div></article>
    <article class="product"><div class="product-photo budder" role="img" aria-label="Golden budder concentrate"></div><h4 class="product-name">Amberline Budder</h4><div class="product-rule"></div><div class="product-price">$40.00</div></article>
  </div>
  <div class="load-more">LOAD MORE</div>
</section>

<section class="testimonials">
  <div class="eyebrow">TESTIMONIALS</div>
  <h2 class="section-title">Our Clients Said</h2>
  <div class="dots"><i></i><i class="on"></i></div>
  <div class="quote" style="left:233px">
    <div class="avatar" role="img" aria-label="Client portrait"></div><span class="quote-mark">”</span>
    <h4>Marco T.</h4><div class="role">CLIENT</div>
    <p>“These guys really know their stuff man.<br>Nothin' but the kind here!”</p>
  </div>
  <div class="quote" style="left:414px">
    <div class="avatar" role="img" aria-label="Client portrait"></div><span class="quote-mark">”</span>
    <h4>Lena R.</h4><div class="role">CLIENT</div>
    <p>“This dispensary has the very best med!<br>I love their meadow haze!”</p>
  </div>
</section>

<footer class="site-footer">
  <div class="col" style="left:97px">
    <h5>CONTACT US</h5>
    <div class="label">Call us 24/7</div>
    <div class="phone">555-017-3348</div>
    <div class="label">Email</div>
    <div class="email">hello@brindlegatecourier.example</div>
    <div class="social"><i style="background:#29a9e0"></i><i style="background:#3b5998"></i><i style="background:#dd4b39"></i><i style="background:#c1358a"></i><i style="background:#cc2020"></i></div>
  </div>
  <div class="col" style="left:233px">
    <h5>QUICK LINKS</h5>
    <ul><li>Store</li><li>Cart</li><li>My Account</li><li>New Patient Verification</li><li>Policy</li><li>Term &amp; Conditions</li></ul>
  </div>
  <div class="col" style="left:369px">
    <h5>FORUMS</h5>
    <ul><li>Bongs, Bubblers, &amp; Water Pipes</li><li>Concentrates</li><li>Growing</li><li>Vaporizers</li><li>What Are You Smokin'?</li></ul>
  </div>
  <div class="col" style="left:505px">
    <h5>NEWSLETTER</h5>
    <p class="news-text">Subscribe to mail list in order to receive fresh deals and coupons directly to your mailbox</p>
    <div class="news-input">Enter your email here...</div>
    <div class="news-btn">SUBSCRIBE</div>
  </div>
  <div class="footer-base">© 2018 Brindlegate. All Rights Reserved.</div>
</footer>

</body>
</html>
```